Small Business Consulting Firm Needs Business Card Design

Need a sleek modern business card with 2 sides matching the colors of our logo. We will be placing these with a mailer we are sending out. These business cards will only ever be given to business owners. We operate helping businesses who are struggling with cash flow or finances. If the green and blue design needs to be moved to the right of "Harborline Crest Consulting" for aesthetic purposes that is ok. We will need an editable file if possible. We would like to include the reps name, email, website, and phone number. For now just use Peter Vance, pvance@harborlinecrest.com, www.harborlinecrest.com, and 833-555-0172.

```html
<!DOCTYPE html>
<html lang="en">
<head>
<meta charset="utf-8">
<title>Harborline Crest Consulting – Business Card</title>
<link href="https://fonts.googleapis.com/css2?family=Arimo:ital,wght@0,400;1,400&family=Montserrat:wght@400&display=swap" rel="stylesheet">
<style>
  :root {
    --backdrop: #f2f2f2;
    --card: #ffffff;
    --ink: #434343;
    --green: #7ab943;
    --green-pale: #d8e9c8;
    --blue-pale: #b6daec;
    --shadow: rgba(0, 0, 0, 0.35);
  }
  * { margin: 0; padding: 0; box-sizing: border-box; }
  html, body {
    width: 1099px;
    height: 1200px;
    overflow: hidden;
    background: var(--backdrop);
  }
  .canvas {
    position: relative;
    width: 1099px;
    height: 1200px;
  }
  .card {
    position: absolute;
    left: 172px;
    width: 755px;
    height: 431px;
    background: var(--card);
    box-shadow: 0 6px 10px var(--shadow);
    overflow: hidden;
  }
  .card--front { top: 139px; }
  .card--back { top: 628px; }

  /* Front */
  .accent {
    position: absolute;
    right: 0;
    top: 0;
    width: 320px;
    height: 431px;
  }
  .rep {
    position: absolute;
    left: 65px;
    top: 146px;
    width: 347px;
    font-family: "Arimo", Arial, sans-serif;
    color: var(--ink);
  }
  .rep__name {
    padding-left: 5px;
    font-size: 29px;
    font-weight: 400;
    line-height: 1.1;
  }
  .rep__company {
    padding-left: 7px;
    margin-top: 6px;
    font-size: 16px;
    font-style: italic;
    line-height: 1.2;
  }
  .rep__rule {
    margin-top: 14px;
    border: 0;
    border-top: 1.5px solid var(--ink);
  }
  .contacts {
    list-style: none;
    margin-top: 36px;
  }
  .contacts li {
    display: flex;
    align-items: baseline;
    height: 43.5px;
  }
  .contacts__label {
    width: 38px;
    font-size: 15px;
  }
  .contacts__value {
    font-size: 21.5px;
  }

  /* Back */
  .brand {
    position: absolute;
    inset: 0;
    display: flex;
    flex-direction: column;
    align-items: center;
    font-family: "Montserrat", Arial, sans-serif;
    font-weight: 400;
    color: var(--ink);
  }
  .brand__square {
    width: 84px;
    height: 84px;
    margin-top: 130px;
    background: var(--green);
  }
  .brand__name {
    margin-top: 52px;
    font-size: 34px;
    letter-spacing: 0.1em;
    line-height: 1;
  }
  .brand__sub {
    margin-top: 18px;
    font-size: 24px;
    letter-spacing: 0.9em;
    margin-right: -0.9em;
    line-height: 1;
  }
</style>
</head>
<body>
<main class="canvas">
  <section class="card card--front" aria-label="Card front">
    <svg class="accent" viewBox="0 0 320 431" aria-hidden="true">
      <rect x="40" y="40" width="330" height="330" fill="var(--green-pale)" opacity="0.8"/>
      <rect x="110" y="110" width="260" height="260" fill="var(--card)"/>
      <rect x="200" y="200" width="140" height="140" fill="var(--blue-pale)"/>
    </svg>
    <div class="rep">
      <h1 class="rep__name">PETER VANCE</h1>
      <p class="rep__company">HARBORLINE CREST CONSULTING</p>
      <hr class="rep__rule">
      <ul class="contacts">
        <li><span class="contacts__label">E:</span><span class="contacts__value">pvance@harborlinecrest.com</span></li>
        <li><span class="contacts__label">W:</span><span class="contacts__value">www.harborlinecrest.com</span></li>
        <li><span class="contacts__label">T:</span><span class="contacts__value">833-555-0172</span></li>
      </ul>
    </div>
  </section>

  <section class="card card--back" aria-label="Card back">
    <div class="brand">
      <div class="brand__square" aria-hidden="true"></div>
      <p class="brand__name">HARBORLINE CREST</p>
      <p class="brand__sub">CONSULTING</p>
    </div>
  </section>
</main>
</body>
</html>
```